Web design for a dental and eye clinic

We need a web design for a dental and eye clinic ( with medical laboratory services) with two branches in Lagos Nigeria. The ultimate aim is to attract more patronage. The design should have links to social media and should have provision for appointments and enquiries. Blue should be part of the colours

Name of facility. VORANTACARE Added Saturday, May 27, 2017

Target Market(s)

Lagos. Nigeria

Industry/Entity Type

Health Care

Number of Pages Required

3 page

Font styles to use
Sans Serif

Colors
85cae6
cadf82

Requirements
Must have
• a projection of the professioal services rendered
Nice to have
• portal for enquiries and appointments
• Link to our facebook, twitter and instagram

```html
<!DOCTYPE html>
<html lang="en">
<head>
<meta charset="utf-8">
<title>Vorantacare – Dental &amp; Eye</title>
<link href="https://fonts.googleapis.com/css2?family=Hind:wght@400;500;600;700&family=Open+Sans:wght@400;600&display=swap" rel="stylesheet">
<style>
:root{
  --sky:#85cae6;
  --lime:#cadf82;
  --navy:#1d3a8a;
  --ink:#111;
  --text:#333;
  --muted:#777;
  --band:#3a8fc0;
  --footer:#1c1c1c;
  --green:#3fb45a;
  --field:#eef3f6;
  --panel:#f2f2f2;
}
*{margin:0;padding:0;box-sizing:border-box}
html,body{width:1200px;height:2400px;overflow:hidden;background:#fff}
body{position:relative;font-family:"Open Sans",sans-serif;color:var(--text)}
.abs{position:absolute}
.head-font{font-family:"Hind",sans-serif}

.top-strip{left:0;top:0;width:1200px;height:16px;background:#e6f2f8}
.header{left:0;top:16px;width:1200px;height:118px;background:#fff}
.brand{left:99px;top:56px;display:flex;align-items:center;gap:12px}
.brand-dot{width:40px;height:40px;border-radius:50%;background:var(--sky)}
.brand-name{font-family:"Hind",sans-serif;font-weight:700;font-size:30px;color:var(--navy)}
.contact-line{top:38px;font-size:14px;color:#555;display:flex;align-items:center;gap:10px}
.nav{top:83px;left:392px;display:flex;font-family:"Hind",sans-serif;font-weight:600;font-size:13px;color:#222;letter-spacing:.3px}
.nav a{position:absolute;white-space:nowrap;color:inherit;text-decoration:none}
.nav .active::after{content:"";position:absolute;left:0;right:0;top:26px;height:2px;background:var(--lime)}
.btn-appoint{left:890px;top:77px;width:187px;height:32px;border-radius:16px;background:var(--sky);color:#fff;font-family:"Hind",sans-serif;font-weight:700;font-size:11px;display:flex;align-items:center;justify-content:center;letter-spacing:.3px}

.hero{left:0;top:134px;width:1200px;height:509px;background:linear-gradient(90deg,#eef3f8 0%,#e4ecf3 45%,#d9c6a8 62%,#c9a77e 78%,#dfe6ee 100%)}
.hero-title{left:99px;top:277px;width:501px;height:64px;background:var(--sky);font-family:"Hind",sans-serif;font-weight:700;font-size:40px;color:#111;padding:6px 0 0 16px;line-height:56px}
.hero-sub{left:99px;top:349px;width:584px;height:53px;background:var(--lime);font-family:"Hind",sans-serif;font-weight:500;font-size:21px;color:#111;padding:0 0 0 18px;line-height:55px}
.slide-label{top:308px;font-size:13px;color:#aab}
.slide-arrow{top:342px}

.welcome-title{left:0;top:686px;width:1200px;text-align:center;font-family:"Hind",sans-serif;font-weight:600;font-size:26px;color:#111}
.welcome-text{left:144px;top:748px;width:912px;text-align:center;font-size:14.5px;line-height:22px;color:#333}

.col-head{top:894px;height:71px;font-family:"Hind",sans-serif;font-weight:500;font-size:26px;color:#111;display:flex;align-items:center;justify-content:center}
.col-head.eye{left:112px;width:496px;background:var(--sky)}
.col-head.dental{left:608px;width:485px;background:var(--lime)}
.col-divider{left:608px;top:965px;width:1px;height:427px;background:#e4e4e4}
.photo{background:#ccc}
.ba-card{background:#fff;box-shadow:0 2px 8px rgba(0,0,0,.18);padding:6px 6px 0}
.ba-card .photo{width:100%;height:144px;background:linear-gradient(135deg,#e79a9a,#c46262)}
.ba-card span{display:block;text-align:center;font-size:10px;font-weight:600;color:#333;padding-top:8px}
.col-text{top:1245px;text-align:center;font-size:13.5px;line-height:17.5px;color:#222}
.btn-read{top:1389px;width:144px;height:38px;background:#e3e3e3;font-family:"Hind",sans-serif;font-size:13px;font-weight:500;color:#222;display:flex;align-items:center;justify-content:center}

.advice{left:0;top:1507px;width:1200px;height:466px;background:var(--panel)}
.advice-photo{left:0;top:1507px;width:620px;height:466px;background:linear-gradient(90deg,#d8e4e8 0%,#eef2f3 55%,rgba(242,242,242,0) 100%)}
.advice-title{left:603px;top:1556px;font-family:"Hind",sans-serif;font-weight:700;font-size:42px;color:#333}
.advice-sub{left:606px;top:1624px;font-size:16px;color:#777}
.field{background:var(--field);border:1px solid #c8cfd4;font-size:12px;color:#888;padding:10px 18px}
.btn-send{left:608px;top:1896px;width:130px;height:32px;background:#3bb5e0;color:#fff;font-family:"Hind",sans-serif;font-weight:700;font-size:10px;display:flex;align-items:center;justify-content:center}

.info-band{left:0;top:1973px;width:1200px;height:109px;background:var(--band)}
.info-item{top:2002px;display:flex;gap:14px;color:#fff}
.info-item h4{font-family:"Hind",sans-serif;font-weight:700;font-size:18px;line-height:20px}
.info-item p{font-size:10px;line-height:16px}

.footer{left:0;top:2082px;width:1200px;height:318px;background:var(--footer)}
.foot-head{top:2148px;font-family:"Hind",sans-serif;font-weight:700;font-size:14px;letter-spacing:1.2px;color:#fff}
.foot-head::after{content:"";display:block;width:26px;height:2px;background:var(--green);margin-top:12px}
.foot-text{left:122px;top:2196px;font-size:13.5px;line-height:23px;color:#bbb}
.foot-list{top:2200px;list-style:none;font-size:13px;color:#bbb}
.foot-list li{height:29px;display:flex;align-items:center;gap:12px}
.foot-list li::before{content:"";width:9px;height:9px;border:2px solid var(--green);border-radius:50%}
.signup-label{left:786px;top:2148px;font-size:13px;color:#ccc}
.signup-input{left:786px;top:2179px;width:288px;height:45px;background:#e3f4f2;font-size:13px;color:#777;padding:14px 18px}
.btn-signup{left:786px;top:2243px;width:107px;height:47px;background:var(--green);color:#fff;font-family:"Hind",sans-serif;font-weight:700;font-size:14px;letter-spacing:1px;display:flex;align-items:center;justify-content:center}
.foot-rule{left:112px;top:2357px;width:950px;height:1px;background:#2e2e2e}
.copyright{left:0;top:2368px;width:1200px;text-align:center;font-size:11px;color:#888}
</style>
</head>
<body>

<div class="abs top-strip"></div>
<header class="abs header"></header>
<div class="abs brand"><span class="brand-dot"></span><span class="brand-name">Vorantacare</span></div>

<div class="abs contact-line" style="left:643px">
  <svg width="16" height="12" viewBox="0 0 16 12"><rect width="16" height="12" rx="1" fill="#5bb85c"/><path d="M0 1l8 6 8-6" stroke="#fff" stroke-width="1.5" fill="none"/></svg>
  info@vorantacare.com
</div>
<div class="abs contact-line" style="left:904px">
  <svg width="16" height="16" viewBox="0 0 24 24"><path fill="#5bb85c" d="M6.6 10.8a15 15 0 006.6 6.6l2.2-2.2c.3-.3.7-.4 1-.2 1.1.4 2.3.6 3.6.6.6 0 1 .4 1 1V20c0 .6-.4 1-1 1A17 17 0 013 4c0-.6.4-1 1-1h3.5c.6 0 1 .4 1 1 0 1.3.2 2.5.6 3.6.1.3 0 .7-.2 1z"/></svg>
  (+234) - 0801 - 4420 - 31
</div>

<nav class="abs nav">
  <a class="active" style="left:0">HOME</a>
  <a style="left:70px">ABOUT US</a>
  <a style="left:166px">SERVICES</a>
  <a style="left:258px">DENTAL</a>
  <a style="left:339px">EYES</a>
  <a style="left:403px">CONTACT</a>
</nav>
<div class="abs btn-appoint">MAKE AN APPOINTMENT</div>

<section class="abs hero" role="img" aria-label="Photo of a young girl covering one eye in front of an eye test chart"></section>
<div class="abs hero-title">CHILDREN'S EYE CARE</div>
<div class="abs hero-sub">SPECIALISTS IN PEDIATRIC &amp; ADULT EYE CARE SERVICES</div>
<div class="abs slide-label" style="left:22px">Eyes</div>
<svg class="abs slide-arrow" style="left:36px" width="16" height="32" viewBox="0 0 16 32"><path d="M14 2L2 16l12 14" stroke="var(--navy)" stroke-width="2.5" fill="none"/></svg>
<div class="abs slide-label" style="left:1128px">Dental</div>
<svg class="abs slide-arrow" style="left:1136px" width="16" height="32" viewBox="0 0 16 32"><path d="M2 2l12 14L2 30" stroke="var(--navy)" stroke-width="2.5" fill="none"/></svg>

<h1 class="abs welcome-title">WELCOME TO VORANTACARE</h1>
<p class="abs welcome-text">Lorem ipsum dolor sit amet, consectetur adipisicing elit, sed do eiusmod tempor incididunt ut labore et dolore magna aliqua. Ut enim ad minim<br>veniam, quis nostrud exercitation ullamco laboris nisi ut aliquip ex ea commodo consequat. Duis aute irure eprehenderit in voluptate esse<br>cillum dolore eu fugiat nulla pariatur. Excepteur sint occaecat cupidatat non proident</p>

<h2 class="abs col-head eye">VORANTACARE EYE</h2>
<h2 class="abs col-head dental">VORANTACARE DENTAL</h2>
<div class="abs col-divider"></div>

<div class="abs ba-card" style="left:213px;top:992px;width:126px;height:180px">
  <div class="photo" role="img" aria-label="Smile before teeth whitening"></div><span>BEFORE</span>
</div>
<div class="abs ba-card" style="left:354px;top:1045px;width:126px;height:180px">
  <div class="photo" role="img" aria-label="Smile after teeth whitening"></div><span>AFTER</span>
</div>
<div class="abs" style="left:326px;top:1070px;width:38px;height:38px;border-radius:50%;background:#2fa6db;border:4px solid #fff"></div>

<div class="abs photo" style="left:661px;top:995px;width:408px;height:197px;background:linear-gradient(90deg,#e8e4e2 0%,#d6cfca 45%,#c79a88 60%,#9c6b58 100%)" role="img" aria-label="Optometrist examining a patient and a close-up eye scan"></div>

<p class="abs col-text" style="left:128px;width:440px">Lorem ipsum dolor sit amet, consectetur adipisicing elit, sed do eiusmod tempor incididunt ut labore et dolore magna aliqua. Ut enim ad minim veniam, quis nostrud exercitation ullamco laboris nisi ut aliquip ex ea commodo consequat.<br><br>Duis aute irure eprehenderit in voluptate esse<br>cillum dolore eu fugiat nulla pariatur.</p>
<p class="abs col-text" style="left:650px;width:443px">Lorem ipsum dolor sit amet, consectetur adipisicing elit, sed do eiusmod tempor incididunt ut labore et dolore magna aliqua. Ut enim ad minim veniam, quis nostrud exercitation ullamco laboris nisi ut aliquip ex ea commodo consequat.<br><br>Duis aute irure eprehenderit in voluptate esse<br>cillum dolore eu fugiat nulla pariatur.</p>
<div class="abs btn-read" style="left:274px">READ MORE</div>
<div class="abs btn-read" style="left:779px">READ MORE</div>

<section class="abs advice"></section>
<div class="abs advice-photo" role="img" aria-label="Photo of a dental treatment chair and instruments"></div>
<h2 class="abs advice-title">Looking for Advice ?</h2>
<p class="abs advice-sub">Your request will be answered withing 24 hours</p>
<div class="abs field" style="left:608px;top:1666px;width:238px;height:41px">Name *</div>
<div class="abs field" style="left:858px;top:1666px;width:238px;height:41px">E-mail *</div>
<div class="abs field" style="left:608px;top:1723px;width:488px;height:144px">Message</div>
<div class="abs btn-send">SEND MESSAGE</div>

<section class="abs info-band"></section>
<div class="abs info-item" style="left:254px">
  <svg width="34" height="46" viewBox="0 0 34 46"><path d="M17 2C9 2 3 8 3 16c0 11 14 27 14 27s14-16 14-27C31 8 25 2 17 2z" stroke="#fff" stroke-width="2" fill="none"/><circle cx="17" cy="16" r="5" stroke="#fff" stroke-width="2" fill="none"/></svg>
  <div><h4>OUR LOCATION</h4><p>B7-Marina Road , Lagos<br>101241 NG</p></div>
</div>
<div class="abs info-item" style="left:518px">
  <svg width="44" height="50" viewBox="0 0 44 50"><rect x="2" y="4" width="12" height="42" rx="3" stroke="#fff" stroke-width="2" fill="none"/><rect x="14" y="8" width="28" height="36" rx="3" stroke="#fff" stroke-width="2" fill="none"/><rect x="20" y="13" width="16" height="8" stroke="#fff" stroke-width="2" fill="none"/><g fill="#fff"><circle cx="22" cy="28" r="1.6"/><circle cx="28" cy="28" r="1.6"/><circle cx="34" cy="28" r="1.6"/><circle cx="22" cy="35" r="1.6"/><circle cx="28" cy="35" r="1.6"/><circle cx="34" cy="35" r="1.6"/></g></svg>
  <div><h4>CALL US</h4><p>1 (802) 418-6630, 552190<br>Customer Support Toll free</p></div>
</div>
<div class="abs info-item" style="left:786px">
  <svg width="44" height="50" viewBox="0 0 44 50"><path d="M3 20l19-16 19 16v27H3z" stroke="#fff" stroke-width="2" fill="none"/><path d="M3 20l19 14 19-14" stroke="#fff" stroke-width="2" fill="none"/><path d="M12 14h20M12 20h20" stroke="#fff" stroke-width="2"/></svg>
  <div><h4>EMAIL US</h4><p>info@vcare.ng<br>Normally respond in 5 - 6 hours</p></div>
</div>

<footer class="abs footer"></footer>
<h5 class="abs foot-head" style="left:122px">HEADQUARTERS</h5>
<p class="abs foot-text">1420 admiralty way. suite 210 lekki lagos<br>ng 106104<br>support@vorantacare.com<br>01 700 455 2290</p>
<h5 class="abs foot-head" style="left:453px">SERVICES</h5>
<ul class="abs foot-list" style="left:455px">
  <li>hourly care</li><li>daily care</li><li>hospital to home</li><li>respite care</li><li>specialized care</li>
</ul>
<h5 class="abs foot-head" style="left:619px">COMPANY</h5>
<ul class="abs foot-list" style="left:621px">
  <li>about us</li><li>locations</li><li>caregivers</li><li>news &amp; blog</li><li>contact us</li>
</ul>
<p class="abs signup-label">sign up to receive the latest articles</p>
<div class="abs signup-input">your email address</div>
<div class="abs btn-signup">SIGN UP</div>
<div class="abs foot-rule"></div>
<p class="abs copyright">Copyright © 2017 Vorantacare Dental &amp; Eye. All rights reserved.</p>

</body>
</html>
```